Bref créative
Letterhead, envelope, business card design
Marlowe Crest Advisory
I need double sided standard sized Business Card [3.5" x 2"]
Use whatever font you think is best
Professional
R. Dwight Folsom, DWMA®
Wealth Advisor
2400 Birchmoor Avenue
Suite 418
Delford, PA 19586
rfolsom@marlowe-crest.example
www.marlowe-crest.example
The following disclosure goes on letterhead at the bottom, on the back of the envelope on the flap, and on the business card.
Securities offered through QVD Brokerage, Member NAXO/BTPE.
Investment advice offered through Harbor Counsel Partners, a registered investment advisor.
Harbor Counsel Partners and Marlowe Crest Advisory are separate entities from QVD Brokerage.
You can either design a one sided business card or a two sided business card. If you design a two sided card, follow these guidelines:
1. Place the address on the back of the card along with the disclosure. Logo, name and title can remain on the front side of the card. OR
2. Place the disclosure on the front of the card and move “nonessential” information such as website address, fax number, etc. to the back.
Existing logo files

```html
<!DOCTYPE html>
<html lang="en">
<head>
<meta charset="utf-8">
<title>Marlowe Crest Advisory — Stationery Set</title>
<link href="https://fonts.googleapis.com/css2?family=Cinzel:wght@700&family=Open+Sans:wght@400;600&display=swap" rel="stylesheet">
<style>
  :root{
    --navy:#1f3b66;
    --navy-deep:#132746;
    --navy-light:#3d6aa3;
    --gold:#e0a24a;
    --paper:#ffffff;
    --ink:#4a5566;
    --bg:#eceae6;
    --line:#c9ced6;
  }
  *{box-sizing:border-box;margin:0;padding:0}
  html,body{width:1200px;height:473px;overflow:hidden}
  body{background:var(--bg);position:relative;font-family:"Open Sans",Arial,sans-serif;color:var(--ink)}
  .sheet{position:absolute;background:var(--paper);box-shadow:0 2px 5px rgba(0,0,0,.18);overflow:hidden}
  .brand{display:flex;align-items:center;gap:4px}
  .brand-dot{width:10px;height:10px;background:var(--navy);border-radius:50%;flex:none}
  .brand-name{font-family:"Cinzel",Georgia,serif;font-weight:700;color:var(--navy);font-size:8px;line-height:1.05;letter-spacing:.02em}
  .letterhead{width:211px;height:288px;top:19px}
  .letterhead .brand{position:absolute;top:12px;left:12px;width:100px}
  .letterhead .brand.center{left:50%;transform:translateX(-50%);justify-content:center}
  .contact{position:absolute;top:12px;right:14px;font-size:3.6px;line-height:1.45;color:var(--ink)}
  .disclosure{position:absolute;bottom:18px;left:0;right:0;text-align:center;font-size:3.2px;line-height:1.5;color:var(--ink)}
  .disclosure.gold{color:#c8904a}
  .rule{position:absolute;left:0;right:0;bottom:8px;height:3px;background:var(--navy)}

  .card{width:108px;height:48px;top:19px}
  .card-front{left:948px}
  .card-front .brand{position:absolute;top:6px;left:6px;gap:3px}
  .card-front .brand-dot{width:7px;height:7px}
  .card-front .brand-name{font-size:5px}
  .card-front .card-person{position:absolute;top:6px;right:6px;text-align:right;font-size:3px;line-height:1.4;color:var(--ink)}
  .card-front .card-person strong{display:block;font-weight:600;color:var(--navy);font-size:3.4px}
  .card-front .card-disclosure{position:absolute;left:4px;right:4px;bottom:7px;text-align:center;font-size:2.1px;line-height:1.35;color:var(--ink)}
  .card-front .rule{bottom:3px;height:2px}
  .card-back{left:1062px;background:linear-gradient(135deg,var(--navy-light),var(--navy-deep));color:#fff}
  .card-back .brand{position:absolute;top:6px;left:50%;transform:translateX(-50%);gap:3px}
  .card-back .brand-dot{width:7px;height:7px;background:#fff}
  .card-back .brand-name{color:#fff;font-size:5px;white-space:nowrap}
  .card-back .card-address{position:absolute;top:17px;left:0;right:0;text-align:center;font-size:2.8px;line-height:1.4}
  .card-back .card-disclosure{position:absolute;left:4px;right:4px;bottom:4px;text-align:center;font-size:2.1px;line-height:1.35;color:#dfe6f0}

  .envelope{height:125px;top:331px}
  .envelope svg{position:absolute;inset:0}
  .envelope .brand{position:absolute;left:50%;transform:translateX(-50%);flex-direction:column;text-align:center}
  .big-envelope{left:943px;top:79px;width:233px;height:204px}
  .big-envelope .brand{position:absolute;top:12px;left:12px}
  .big-envelope .contact{left:12px;right:auto;top:36px}
  .big-envelope svg{position:absolute;left:0;bottom:0}
  .flap-back{left:980px;top:331px;width:196px;height:125px}
  .flap-back .disclosure{top:14px;bottom:auto}
</style>
</head>
<body>

<section class="sheet letterhead" style="left:29px">
  <div class="brand"><span class="brand-dot"></span><span class="brand-name">Marlowe Crest<br>Advisory</span></div>
  <div class="contact">R. Dwight Folsom, DWMA®<br>Wealth Advisor<br>2400 Birchmoor Avenue<br>Suite 418<br>Delford, PA 19586<br>rfolsom@marlowe-crest.example<br>www.marlowe-crest.example</div>
  <p class="disclosure">Securities offered through QVD Brokerage, Member NAXO/BTPE.<br>Investment advice offered through Harbor Counsel Partners, a registered investment advisor.<br>Harbor Counsel Partners and Marlowe Crest Advisory are separate entities from QVD Brokerage.</p>
  <div class="rule"></div>
</section>

<section class="sheet letterhead" style="left:254px">
  <div class="brand"><span class="brand-dot"></span><span class="brand-name">Marlowe Crest<br>Advisory</span></div>
  <div class="contact">R. Dwight Folsom, DWMA®<br>Wealth Advisor<br>2400 Birchmoor Avenue<br>Suite 418<br>Delford, PA 19586<br>rfolsom@marlowe-crest.example<br>www.marlowe-crest.example</div>
  <p class="disclosure gold">Securities offered through QVD Brokerage, Member NAXO/BTPE.<br>Investment advice offered through Harbor Counsel Partners, a registered investment advisor.<br>Harbor Counsel Partners and Marlowe Crest Advisory are separate entities from QVD Brokerage.</p>
  <div class="rule"></div>
</section>

<section class="sheet letterhead" style="left:475px">
  <div class="brand center"><span class="brand-dot"></span><span class="brand-name">Marlowe Crest Advisory</span></div>
  <p class="disclosure" style="bottom:28px">R. Dwight Folsom, DWMA® · Wealth Advisor · 2400 Birchmoor Avenue, Suite 418, Delford, PA 19586<br>Securities offered through QVD Brokerage, Member NAXO/BTPE.<br>Investment advice offered through Harbor Counsel Partners, a registered investment advisor.<br>Harbor Counsel Partners and Marlowe Crest Advisory are separate entities from QVD Brokerage.</p>
  <div class="rule" style="background:var(--gold);height:2px"></div>
</section>

<section class="sheet letterhead" style="left:701px">
  <div class="brand center"><span class="brand-dot"></span><span class="brand-name">Marlowe Crest Advisory</span></div>
  <p class="disclosure" style="bottom:28px">R. Dwight Folsom, DWMA® · Wealth Advisor · 2400 Birchmoor Avenue, Suite 418, Delford, PA 19586<br>Securities offered through QVD Brokerage, Member NAXO/BTPE.<br>Investment advice offered through Harbor Counsel Partners, a registered investment advisor.<br>Harbor Counsel Partners and Marlowe Crest Advisory are separate entities from QVD Brokerage.</p>
  <div class="rule"></div>
</section>

<section class="sheet card card-front">
  <div class="brand"><span class="brand-dot"></span><span class="brand-name">Marlowe Crest<br>Advisory</span></div>
  <div class="card-person"><strong>R. Dwight Folsom, DWMA®</strong>Wealth Advisor<br>rfolsom@marlowe-crest.example<br>www.marlowe-crest.example</div>
  <p class="card-disclosure">Securities offered through QVD Brokerage, Member NAXO/BTPE.<br>Investment advice offered through Harbor Counsel Partners, a registered investment advisor.<br>Harbor Counsel Partners and Marlowe Crest Advisory are separate entities from QVD Brokerage.</p>
  <div class="rule"></div>
</section>
<section class="sheet card card-back">
  <div class="brand"><span class="brand-dot"></span><span class="brand-name">Marlowe Crest Advisory</span></div>
  <p class="card-address">2400 Birchmoor Avenue, Suite 418<br>Delford, PA 19586</p>
  <p class="card-disclosure">Securities offered through QVD Brokerage, Member NAXO/BTPE.<br>Investment advice offered through Harbor Counsel Partners, a registered investment advisor.<br>Harbor Counsel Partners and Marlowe Crest Advisory are separate entities from QVD Brokerage.</p>
</section>

<section class="sheet big-envelope">
  <div class="brand"><span class="brand-dot"></span><span class="brand-name">Marlowe Crest<br>Advisory</span></div>
  <div class="contact">2400 Birchmoor Avenue<br>Suite 418<br>Delford, PA 19586</div>
  <svg width="233" height="110" viewBox="0 0 233 110" aria-hidden="true">
    <defs><linearGradient id="bandA" x1="0" y1="0" x2="0" y2="1"><stop offset="0" stop-color="#3d6aa3"/><stop offset="1" stop-color="#132746"/></linearGradient></defs>
    <path d="M0 0 Q116 70 233 0 V110 H0Z" fill="url(#bandA)"/>
    <path d="M0 0 Q116 70 233 0" fill="none" stroke="#ffffff" stroke-width="1.5"/>
  </svg>
</section>

<section class="sheet envelope" style="left:19px;width:228px">
  <svg width="228" height="125" viewBox="0 0 228 125" aria-hidden="true"><path d="M0 0 L114 52 L228 0" fill="none" stroke="var(--line)" stroke-width="1"/></svg>
  <div class="brand" style="top:58px"><span class="brand-dot"></span><span class="brand-name">Marlowe Crest</span></div>
</section>

<section class="sheet envelope" style="left:264px;width:221px">
  <svg width="221" height="125" viewBox="0 0 221 125" aria-hidden="true">
    <defs><linearGradient id="bandB" x1="0" y1="0" x2="0" y2="1"><stop offset="0" stop-color="#132746"/><stop offset="1" stop-color="#3d6aa3"/></linearGradient></defs>
    <path d="M0 0 H221 V22 Q110 80 0 22Z" fill="url(#bandB)"/>
  </svg>
  <div class="brand" style="top:62px"><span class="brand-dot"></span><span class="brand-name">Marlowe Crest</span></div>
</section>

<section class="sheet envelope" style="left:499px;width:233px">
  <svg width="233" height="125" viewBox="0 0 233 125" aria-hidden="true">
    <defs><radialGradient id="bandC" cx=".5" cy=".2" r=".7"><stop offset="0" stop-color="#4b7bb6"/><stop offset="1" stop-color="#132746"/></radialGradient></defs>
    <path d="M0 0 H233 V14 Q116 90 0 14Z" fill="url(#bandC)"/>
  </svg>
  <div class="brand" style="top:14px"><span class="brand-dot" style="background:#fff"></span></div>
</section>

<section class="sheet envelope" style="left:746px;width:219px">
  <svg width="219" height="125" viewBox="0 0 219 125" aria-hidden="true"><path d="M0 0 L109 56 L219 0" fill="none" stroke="var(--line)" stroke-width="1"/></svg>
</section>

<section class="sheet envelope flap-back">
  <p class="disclosure">Securities offered through QVD Brokerage, Member NAXO/BTPE.<br>Investment advice offered through Harbor Counsel Partners, a registered investment advisor.<br>Harbor Counsel Partners and Marlowe Crest Advisory are separate entities from QVD Brokerage.</p>
  <svg width="196" height="125" viewBox="0 0 196 125" aria-hidden="true"><path d="M0 0 L98 44 L196 0" fill="none" stroke="var(--line)" stroke-width="1"/></svg>
</section>

</body>
</html>
```